Business Card Design Project

Hello
I want a Simple Business card that uses the company logo that is easily reasonable but looks professional as I am an IT Services company and would look to share these cards with prospective clients.
The details are:
Kestrel Arc Solutions
14 Morrow Lane
Birmingham
B7 4QX
Telephone 0845 217 6640
I would like my name Oliver Hastings and my title Director on the card.
Target Market(s)
IT Professionals
Industry/Entity Type
Business

```html
<!DOCTYPE html>
<html lang="en">
<head>
<meta charset="utf-8">
<title>Kestrel Arc Solutions – Business Card</title>
<link rel="stylesheet" href="https://fonts.googleapis.com/css2?family=PT+Serif:wght@400;700&display=swap">
<style>
  :root {
    --backdrop: #e8e5e1;
    --card: #ffffff;
    --ink: #222222;
    --accent-green: #a8d05c;
    --mark-green: #8cc46a;
  }
  html, body {
    margin: 0;
    padding: 0;
    width: 1200px;
    height: 961px;
    overflow: hidden;
    background: var(--backdrop);
  }
  .stage {
    position: relative;
    width: 1200px;
    height: 961px;
  }
  .business-card {
    position: absolute;
    left: 250px;
    top: 282px;
    width: 712px;
    height: 405px;
    background: var(--card);
    box-shadow: 0 2px 6px rgba(0,0,0,0.18);
    font-family: "PT Serif", Georgia, serif;
    color: var(--ink);
  }
  .brand {
    position: absolute;
    left: 0;
    right: 0;
    top: 150px;
    display: flex;
    justify-content: center;
    align-items: center;
    gap: 14px;
  }
  .brand-dot {
    width: 30px;
    height: 30px;
    border-radius: 50%;
    background: var(--mark-green);
  }
  .brand-name {
    font-size: 40px;
    font-weight: 700;
    color: var(--ink);
    line-height: 1;
  }
  .divider {
    position: absolute;
    left: 0;
    right: 0;
    top: 234px;
    height: 3px;
    background: var(--accent-green);
  }
  .holder {
    position: absolute;
    left: 30px;
    top: 292px;
    font-size: 21px;
    font-weight: 700;
    line-height: 27px;
  }
  .contact {
    position: absolute;
    right: 38px;
    top: 265px;
    text-align: right;
    font-size: 21px;
    line-height: 27px;
  }
  .contact p { margin: 0; }
  .phone {
    font-weight: 700;
    display: flex;
    align-items: center;
    justify-content: flex-end;
    gap: 4px;
    margin-top: 2px !important;
  }
  .phone-icon { width: 30px; height: 38px; }
</style>
</head>
<body>
<main class="stage">
  <section class="business-card">
    <div class="brand">
      <span class="brand-dot"></span>
      <span class="brand-name">Kestrel Arc Solutions</span>
    </div>
    <div class="divider"></div>
    <div class="holder">
      <p style="margin:0">Oliver Hastings</p>
      <p style="margin:0">Director</p>
    </div>
    <address class="contact" style="font-style:normal">
      <p>14 Morrow Lane</p>
      <p>Birmingham</p>
      <p>B7 4QX</p>
      <p class="phone">
        <svg class="phone-icon" viewBox="0 0 30 38" aria-hidden="true">
          <rect x="7" y="5" width="14" height="28" rx="3" transform="rotate(22 14 19)" fill="none" stroke="#222" stroke-width="2.4"/>
          <circle cx="22" cy="3" r="1.6" fill="none" stroke="#222" stroke-width="1"/>
        </svg>
        <span>0845 217 6640</span>
      </p>
    </address>
  </section>
</main>
</body>
</html>
```